The Lantern Protocol: A Practical Guide for Tending Old Orchards

This will be for both the hard cover and paperback version. A core theme of the book and what we want to cover to convey is the journey or transformation to "happiness". Concepts such as road/pathway, mountain top, sunrise, dark to bright colors, out-of-focus to in-focus, clouds parting, etc., all represent this idea. I am attaching a 1-page book summary for more information. I like the idea of the subtitle being in a gold seal, but that is not necessary. I am open to any designs, but it should at least be conceptually related to the book.

```html
<!DOCTYPE html>
<html lang="en">
<head>
<meta charset="utf-8">
<title>The Lantern Protocol — Book Cover</title>
<link rel="stylesheet" href="https://fonts.googleapis.com/css2?family=PT+Serif:ital,wght@0,400;0,700;1,400;1,700&display=swap">
<style>
  :root {
    --sky-deep: #1d5aa3;
    --sky-mid: #4f8fcf;
    --sky-light: #a9cbea;
    --cloud: #eef3f9;
    --cloud-white: #ffffff;
    --title-white: #ffffff;
    --ink-navy: #2f3d72;
    --feature-warm: rgba(250, 226, 150, 0.55);
    --feature-cool: rgba(190, 205, 215, 0.45);
  }
  html, body {
    margin: 0;
    padding: 0;
    width: 960px;
    height: 1200px;
    overflow: hidden;
    background: #ffffff;
  }
  .cover {
    position: relative;
    width: 960px;
    height: 1200px;
    overflow: hidden;
    font-family: "PT Serif", Georgia, serif;
  }
  .sky-backdrop {
    position: absolute;
    inset: 0;
    background:
      radial-gradient(ellipse 70% 30% at 10% 25%, rgba(255,255,255,0.55), transparent 70%),
      radial-gradient(ellipse 80% 25% at 85% 48%, rgba(255,255,255,0.35), transparent 70%),
      linear-gradient(180deg,
        var(--sky-deep) 0%,
        var(--sky-mid) 30%,
        var(--sky-light) 55%,
        var(--cloud) 75%,
        var(--cloud-white) 90%,
        var(--cloud) 100%);
  }
  .feature-image {
    position: absolute;
    left: 348px;
    top: 390px;
    width: 262px;
    height: 425px;
    background: linear-gradient(180deg, var(--feature-warm) 0%, var(--feature-cool) 100%);
  }
  .title {
    position: absolute;
    left: 0;
    right: 0;
    top: 0;
    margin: 0;
    text-align: center;
    color: var(--title-white);
    font-weight: 700;
    font-style: italic;
    font-size: 100px;
    letter-spacing: 0.13em;
    line-height: 1;
    text-shadow: 0 2px 6px rgba(20, 50, 100, 0.25);
  }
  .title-line {
    position: absolute;
    left: 0;
    right: 0;
    display: block;
    padding-left: 0.13em;
  }
  .title-line--1 { top: 70px; }
  .title-line--2 { top: 188px; }
  .title-line--3 { top: 308px; }
  .subtitle {
    position: absolute;
    left: 0;
    right: 0;
    top: 860px;
    margin: 0;
    text-align: center;
    color: var(--ink-navy);
    font-style: italic;
    font-weight: 400;
    font-size: 44px;
    letter-spacing: 0.1em;
    line-height: 66px;
  }
  .author {
    position: absolute;
    left: 0;
    right: 0;
    top: 1060px;
    margin: 0;
    text-align: center;
    color: var(--ink-navy);
    font-style: italic;
    font-weight: 700;
    font-size: 62px;
    letter-spacing: 0.1em;
    line-height: 1;
  }
</style>
</head>
<body>
  <main class="cover">
    <div class="sky-backdrop" role="img" aria-label="Photograph of a bright blue sky above a sea of white clouds, with faint hand-drawn doodles of life goals"></div>

    <div class="feature-image" role="img" aria-label="Photograph of a glowing light bulb floating above the clouds"></div>

    <h1 class="title">
      <span class="title-line title-line--1">THE</span>
      <span class="title-line title-line--2">LANTERN</span>
      <span class="title-line title-line--3">PROTOCOL</span>
    </h1>

    <p class="subtitle">A Practical Guide for Tending<br>Old Orchards</p>

    <p class="author">Martin J. Halloway</p>
  </main>
</body>
</html>
```